Professional Modern Website Design

We are a premium IT services provider to the financial industry based in London. Our company is called Veltra our current holding page is www.veltra-example.co.uk. We require a new website to match our new corporate identity. This project is for the design phase only. Development will be handled in-house. I have attached examples of wire frames we have developed (although open to suggestions for improvement) Our brand document that should demonstrate current brand, inc how we communicate to potential clients and finally mostly completed web-content.
We are looking for designers that can create something that sets us apart from our competitors.
Target Market(s)
IT Decision makers in Finance companies such as; hedge funds, private investment banks etc
Industry/Entity Type
Financial
Number of Pages Required
5+ page
Requirements
Must have
- hexagon elements in the design, unique design.
Nice to have
- Blog and social media feeds
Should not have
- Should not resemble a downloaded template

```html
<!DOCTYPE html>
<html lang="en">
<head>
<meta charset="utf-8">
<title>Veltra — IT Integration for Finance</title>
<link href="https://fonts.googleapis.com/css2?family=Advent+Pro:wght@300;400&family=Arimo:wght@400&display=swap" rel="stylesheet">
<style>
:root{
  --orange:#f26322;
  --orange-soft:#f39a4e;
  --orange-menu:#f0883a;
  --dark:#1c1c1c;
  --dark-band:#232323;
  --light:#ebebeb;
  --panel:#e0e0e0;
  --text:#3f3f3f;
  --ink:#1a1a1a;
  --footer:#3a3a3a;
  --white:#ffffff;
}
*{margin:0;padding:0;box-sizing:border-box}
html,body{width:796px;height:1200px;overflow:hidden;background:var(--white)}
body{position:relative;font-family:"Arimo",Arial,sans-serif;color:var(--text)}
.display{font-family:"Advent Pro",sans-serif;font-weight:400}

.site-header{position:absolute;left:0;top:0;width:796px;height:143px;background:var(--dark)}
.header-inner{position:absolute;left:66px;top:0;width:663px;height:143px;background:linear-gradient(#1a1a1a,#262626)}
.brand{position:absolute;left:0;top:28px;width:796px;text-align:center}
.brand-mark{display:block;width:44px;height:44px;margin:0 auto 18px;background:var(--orange)}
.brand-name{font-family:"Advent Pro",sans-serif;font-weight:400;font-size:17px;letter-spacing:6px;color:#e8e8e8}

.main-nav{position:absolute;left:0;top:143px;width:796px;height:31px;background:var(--orange)}
.main-nav a{position:absolute;top:0;height:31px;line-height:31px;font-size:12px;color:var(--white);text-decoration:none;transform:translateX(-50%)}
.main-nav a.active{left:384px;width:84px;text-align:center;background:var(--orange-soft)}

.hero-backdrop{position:absolute;left:0;top:174px;width:796px;height:188px;background:var(--dark-band)}
.page-band{position:absolute;left:0;top:362px;width:796px;height:284px;background:var(--light)}
.hero-visual{position:absolute;left:66px;top:174px;width:663px;height:286px;background:linear-gradient(100deg,#2b2b2b 0%,#6f6f6f 35%,#3c3c3c 60%,#2a2a2a 80%,#4d4d4d 100%)}
.hero-card{position:absolute;left:97px;top:234px;width:257px;height:164px;background:rgba(200,200,200,.82);border-radius:6px;padding:16px 12px}
.hero-card h1{font-size:19.5px;line-height:24px;color:var(--ink);font-weight:400;margin-bottom:12px}
.hero-card p{font-size:10.3px;line-height:13.3px;color:#222}

.submenu{position:absolute;left:342px;top:175px;width:167px;list-style:none}
.submenu li{height:24px;line-height:24px;padding-left:9px;font-size:9.5px;color:var(--white);background:var(--orange-menu);border-bottom:1px solid #c9692a}

.intro{position:absolute;left:0;top:488px;width:796px;text-align:center}
.intro h2{font-size:47px;font-weight:300;color:var(--ink);letter-spacing:1px;line-height:56px}
.intro p{margin-top:18px;font-size:11.5px;line-height:17.6px;color:#222}

.roles{position:absolute;left:0;top:646px;width:796px;height:496px}
.role{position:absolute;top:0;text-align:center}
.role .hex{position:absolute;top:45px;width:124px;height:140px}
.role h3{position:absolute;font-size:16px;font-weight:400;line-height:20px;color:var(--ink);width:100%}
.role p{position:absolute;font-size:10.4px;line-height:13.3px;text-align:justify;text-align-last:center;hyphens:auto}
.role.featured h3{color:var(--orange);font-size:20px}
.featured-panel{position:absolute;left:238px;top:26px}
.cta{position:absolute;left:238px;top:438px;width:156px;height:34px;line-height:34px;background:var(--orange);color:var(--white);font-size:10.5px;text-align:center;text-decoration:none}

.site-footer{position:absolute;left:0;top:1142px;width:796px;height:58px;background:var(--footer);color:var(--white);text-align:center}
.footer-links{padding-top:13px;font-size:8.5px;word-spacing:2px}
.footer-links span{margin:0 12px;color:#ddd}
.copyright{margin-top:7px;font-size:9.5px}
</style>
</head>
<body>

<header class="site-header">
  <div class="header-inner"></div>
  <div class="brand"><span class="brand-mark"></span><span class="brand-name">VELTRA</span></div>
</header>

<nav class="main-nav">
  <a style="left:286px">ABOUT</a>
  <a class="active" style="left:384px;transform:translateX(-50%)">SERVICES</a>
  <a style="left:494px">PARTNERS</a>
  <a style="left:594px">CLIENTS</a>
  <a style="left:692px">CONTACT</a>
</nav>

<div class="hero-backdrop"></div>
<div class="page-band"></div>
<div class="hero-visual" role="img" aria-label="Black and white night city skyline with a smiling businessman holding a pen at a desk"></div>

<section class="hero-card">
  <h1 class="display">YOU NEED INTEGRATION. WE'RE ALWAYS THERE WITH YOU.</h1>
  <p>Veltra is one of the leading systems integrators to the world's finance sector. We are an extension of your business and our services portfolio has been built so you always have access to a complete partner.</p>
</section>

<ul class="submenu">
  <li>Data center &amp; infrastructure</li>
  <li>Support,managed &amp; services</li>
  <li>Voice and data</li>
  <li>Hosting and cloud</li>
  <li>Security and IRM</li>
</ul>

<section class="intro">
  <h2 class="display">WHO ARE YOU?</h2>
  <p>If you're part of a financial organisation, we have the power to help everyone work more<br>efficiently, productively and profitably.</p>
</section>

<section class="roles">
  <svg class="featured-panel" width="156" height="412" viewBox="0 0 156 412">
    <polygon points="78,0 156,38 156,412 0,412 0,38" fill="#e0e0e0"/>
  </svg>

  <div class="role" style="left:74px;width:136px">
    <svg class="hex" style="left:6px" viewBox="0 0 124 140" role="img" aria-label="Portrait of a senior executive in a suit">
      <defs><linearGradient id="g1" x1="0" y1="0" x2="1" y2="1"><stop offset="0" stop-color="#c9c9c9"/><stop offset="1" stop-color="#3a3a3a"/></linearGradient></defs>
      <polygon points="62,2 122,36 122,104 62,138 2,104 2,36" fill="url(#g1)" stroke="#555" stroke-width="1.5"/>
    </svg>
    <h3 class="display" style="top:208px">SENIOR HEDGE FUND MANAGER/CEO</h3>
    <p style="top:253px;left:0;width:136px">You need to develop and implement strategies for business growth, while ensuring profitability. You're aware your biggest asset is your staff and a happy workforce is a productive one. Security is a key concern in a changing always-on world and you need to be compliant, but you don't want to overspend. Veltra can help you find the best solutions to help your business grow at the speed you want it to.</p>
  </div>

  <div class="role featured" style="left:249px;width:133px">
    <svg class="hex" style="left:5px" viewBox="0 0 124 140" role="img" aria-label="Hands signing a document at a desk">
      <defs><linearGradient id="g2" x1="0" y1="0" x2="0" y2="1"><stop offset="0" stop-color="#6b6b6b"/><stop offset="1" stop-color="#f2f2f2"/></linearGradient></defs>
      <polygon points="62,2 122,36 122,104 62,138 2,104 2,36" fill="url(#g2)" stroke="#555" stroke-width="1.5"/>
    </svg>
    <h3 class="display" style="top:197px">CFO</h3>
    <p style="top:232px;left:0;width:133px">Your key responsibility is to obtain the maximum ROI from products and services. You understand investment opportunities, providing they return higher efficiencies and revenues. You are concerned more with long-term spending versus short-term and how you can get the most value out of a proposition. Veltra can advise how to boost ROI by streamlining your business to maximise return</p>
  </div>
  <a class="cta">View details →</a>

  <div class="role" style="left:418px;width:133px">
    <svg class="hex" style="left:5px" viewBox="0 0 124 140" role="img" aria-label="Group of IT managers speaking at a conference">
      <defs><linearGradient id="g3" x1="0" y1="0" x2="1" y2="1"><stop offset="0" stop-color="#8a8a8a"/><stop offset="1" stop-color="#2e2e2e"/></linearGradient></defs>
      <polygon points="62,2 122,36 122,104 62,138 2,104 2,36" fill="url(#g3)" stroke="#555" stroke-width="1.5"/>
    </svg>
    <h3 class="display" style="top:216px">IT MANAGER/CTO</h3>
    <p style="top:253px;left:0;width:133px">Integration with partners and services is your key concern. You want to make sure any IT system you implement will work with the whole infrastructure of your company. You don't want your team to waste valuable time dealing with things that don't matter. Veltra provides the whole picture to ensure your company is ready for the next generation of IT</p>
  </div>

  <div class="role" style="left:592px;width:133px">
    <svg class="hex" style="left:5px" viewBox="0 0 124 140" role="img" aria-label="Two smiling colleagues working together in an office">
      <defs><linearGradient id="g4" x1="0" y1="0" x2="1" y2="1"><stop offset="0" stop-color="#d8d8d8"/><stop offset="1" stop-color="#4a4a4a"/></linearGradient></defs>
      <polygon points="62,2 122,36 122,104 62,138 2,104 2,36" fill="url(#g4)" stroke="#555" stroke-width="1.5"/>
    </svg>
    <h3 class="display" style="top:216px">EMPLOAYEE</h3>
    <p style="top:253px;left:0;width:133px">You're working hard, but not getting anywhere fast. You want the tools to make your job easier so you can spend more time thinking about what you're doing rather than how you're doing it. You shouldn't have to think about the technology you're using, because it should just work. Veltra can help you get back on track everyday.</p>
  </div>
</section>

<footer class="site-footer">
  <div class="footer-links">HOME<span>|</span>ABOUT<span>|</span>SERVICES<span>|</span>PARTNERS<span>|</span>CLIENTS<span>|</span>CONTACT</div>
  <div class="copyright">© 2015 veltra-example.com.au . All Rights Reserved</div>
</footer>

</body>
</html>
```